Gentleman's grooming products require a business card

I need a business card that incorporates the logo [ or parts of ] that we had Pixel Hive design for us as uploaded.

We sell online, mens grooming products including moustache waxes, beard oils and shaving accessories.
We want a card that is classy, professional and a card that shouts mens products.

Target Market(s)

Young professional male market

Industry/Entity Type

Business

Contact Information for Business Card

Ross and Edith Carwell
Lather and Lore
Purveyors of gentleman's stiffeners and grooming requisites
M :0418529647
E : ross@latherandlore.com.au
E : edith@latherandlore.com.au
E : sales@theblokesbalmery.com.au

W : www.latherandlore.com.au

Requirements
Must have
• Class
Nice to have
• Professionalism

```html
<!DOCTYPE html>
<html lang="en">
<head>
<meta charset="utf-8">
<title>Lather and Lore — Business Card</title>
<link rel="stylesheet" href="https://fonts.googleapis.com/css2?family=Cinzel:wght@400;600&family=Montserrat:wght@400;500&display=swap">
<style>
  :root {
    --backdrop: #2b2b2d;
    --card: #0d0d0e;
    --ink-white: #f2f2f2;
    --ink-grey: #bdbdbd;
    --rule: #9a9a9a;
    --gold: #e0a92a;
  }
  html, body {
    margin: 0;
    padding: 0;
    width: 1200px;
    height: 900px;
    overflow: hidden;
    background: var(--backdrop);
  }
  .business-card {
    position: absolute;
    left: 170px;
    top: 205px;
    width: 860px;
    height: 490px;
    border-radius: 30px;
    background: var(--card);
    box-shadow: 0 20px 50px rgba(0,0,0,0.55);
    font-family: "Montserrat", sans-serif;
    color: var(--ink-grey);
  }
  .brand-mark {
    position: absolute;
    left: 390px;
    top: 52px;
    width: 64px;
    height: 64px;
    background: var(--ink-white);
  }
  .rule {
    position: absolute;
    height: 1.5px;
    background: var(--rule);
  }
  .rule-top { left: 462px; top: 100px; width: 230px; }
  .rule-mid { left: 168px; top: 184px; width: 524px; }
  .rule-low { left: 168px; top: 300px; width: 524px; }
  .brand-name {
    position: absolute;
    left: 0;
    width: 860px;
    top: 118px;
    text-align: center;
    font-family: "Cinzel", serif;
    font-weight: 400;
    font-size: 50px;
    line-height: 60px;
    color: var(--ink-white);
    margin: 0;
  }
  .tagline {
    position: absolute;
    left: 0;
    width: 860px;
    top: 194px;
    text-align: center;
    font-family: "Cinzel", serif;
    font-size: 12.5px;
    letter-spacing: 1.6px;
    color: var(--ink-white);
    margin: 0;
  }
  .owners {
    position: absolute;
    left: 0;
    width: 860px;
    top: 222px;
    text-align: center;
    margin: 0;
  }
  .owners-first {
    display: block;
    font-size: 15px;
    letter-spacing: 9px;
    color: var(--ink-white);
    text-transform: uppercase;
  }
  .owners-surname {
    display: block;
    margin-top: 4px;
    font-size: 30px;
    font-weight: 500;
    letter-spacing: 20px;
    color: var(--gold);
    text-transform: uppercase;
  }
  .contact-list {
    position: absolute;
    left: 0;
    width: 860px;
    top: 320px;
    margin: 0;
    padding: 0;
    list-style: none;
    text-align: center;
  }
  .contact-row {
    display: block;
    margin-bottom: 12px;
  }
  .contact-item {
    display: inline-flex;
    align-items: center;
    gap: 7px;
    margin: 0 9px;
    font-size: 17px;
    color: var(--ink-grey);
  }
  .contact-icon {
    width: 18px;
    height: 18px;
    flex: none;
  }
</style>
</head>
<body>
  <article class="business-card">
    <div class="brand-mark"></div>
    <div class="rule rule-top"></div>
    <h1 class="brand-name">Lather and Lore</h1>
    <div class="rule rule-mid"></div>
    <p class="tagline">PURVEYORS OF GENTLEMEN'S STIFFENERS AND GROOMING REQUISITES</p>
    <p class="owners">
      <span class="owners-first">Ross &amp; Edith</span>
      <span class="owners-surname">Carwell</span>
    </p>
    <div class="rule rule-low"></div>
    <ul class="contact-list">
      <li class="contact-row">
        <span class="contact-item">
          <svg class="contact-icon" viewBox="0 0 18 18"><rect x="1" y="4" width="16" height="11" fill="var(--gold)"/><path d="M1 4 L9 10 L17 4" stroke="var(--card)" stroke-width="1.3" fill="none"/></svg>
          ross@latherandlore.com.au
        </span>
        <span class="contact-item">
          <svg class="contact-icon" viewBox="0 0 18 18"><rect x="1" y="4" width="16" height="11" fill="var(--gold)"/><path d="M1 4 L9 10 L17 4" stroke="var(--card)" stroke-width="1.3" fill="none"/></svg>
          edith@latherandlore.com.au
        </span>
        <span class="contact-item">
          <svg class="contact-icon" viewBox="0 0 18 18"><rect x="4.5" y="1" width="9" height="16" rx="1.5" fill="var(--gold)"/><rect x="6" y="3" width="6" height="10" fill="var(--card)"/></svg>
          0418 529 647
        </span>
      </li>
      <li class="contact-row">
        <span class="contact-item">
          <svg class="contact-icon" viewBox="0 0 18 18"><rect x="1" y="4" width="16" height="11" fill="var(--gold)"/><path d="M1 4 L9 10 L17 4" stroke="var(--card)" stroke-width="1.3" fill="none"/></svg>
          sales@theblokesbalmery.com.au
        </span>
        <span class="contact-item">
          <svg class="contact-icon" viewBox="0 0 18 18"><circle cx="9" cy="9" r="8" fill="var(--gold)"/><g stroke="var(--card)" stroke-width="1" fill="none"><ellipse cx="9" cy="9" rx="3.5" ry="8"/><path d="M1 9 H17 M2.5 5 H15.5 M2.5 13 H15.5"/></g></svg>
          www.latherandlore.com.au
        </span>
      </li>
    </ul>
  </article>
</body>
</html>
```